Tabletop Sign for Support Coordination Service

We need a design for a table top sign for a Support Coordination enterprise. We find and coordinate support services for those with various disabilities. We would like designs that incorporate our logo and colors, blues and greens as seen in the file upload. Additionally, we would also preferably like designs with a more modern feel. The final design should include all these in addition to our contact information (email and telephone).

```html
<!DOCTYPE html>
<html lang="en">
<head>
<meta charset="utf-8">
<title>Lumen Support Services – Tabletop Sign</title>
<link rel="stylesheet" href="https://fonts.googleapis.com/css2?family=Montserrat:wght@500;600;700;800&display=swap">
<style>
  :root {
    --page-bg: #e1e1e1;
    --brand-blue: #123f6b;
    --brand-green: #6cc04a;
    --white: #ffffff;
    --photo-light: #f4f4f4;
    --photo-mid: #dcdcdc;
    --dot: rgba(255,255,255,0.85);
  }
  * { box-sizing: border-box; margin: 0; padding: 0; }
  html, body {
    width: 1200px; height: 1200px; overflow: hidden;
    background: var(--page-bg);
    font-family: "Montserrat", Arial, sans-serif;
  }
  .sign {
    position: absolute; left: 209px; top: 60px;
    width: 782px; height: 1080px; overflow: hidden;
    background: var(--white);
  }
  .sign__photo {
    position: absolute; inset: 0 0 380px 0;
    background:
      radial-gradient(ellipse at 68% 45%, #c9c9c9 0%, rgba(220,220,220,0.6) 35%, rgba(244,244,244,0) 70%),
      linear-gradient(180deg, var(--photo-light) 0%, var(--photo-mid) 100%);
  }
  .brand { position: absolute; left: 41px; top: 48px; width: 300px; }
  .brand__dot {
    position: absolute; left: 82px; top: 4px;
    width: 104px; height: 104px; border-radius: 50%;
    background: var(--brand-blue);
  }
  .brand__name {
    position: absolute; left: 0; top: 124px;
    font-weight: 800; font-size: 84px; line-height: 1;
    color: var(--brand-green); letter-spacing: -1px;
  }
  .headline {
    position: absolute; left: 0; right: 0; top: 355px;
    text-align: center; font-weight: 700; font-size: 54px;
    color: var(--brand-blue); letter-spacing: 0.3px;
  }
  .service-pill {
    position: absolute; left: 180px; top: 443px;
    width: 421px; height: 50px; border-radius: 16px;
    background: var(--brand-green); border: 2px solid var(--brand-blue);
    color: var(--white); font-weight: 600; font-size: 33px;
    display: flex; align-items: center; justify-content: center;
  }
  .tagline {
    position: absolute; left: 0; right: 0; top: 520px;
    text-align: center; font-weight: 600; font-size: 30px;
    color: var(--brand-blue);
  }
  .waves { position: absolute; left: 0; top: 0; }
  .contact { position: absolute; left: 0; right: 0; text-align: center; }
  .contact__email {
    top: 754px; font-weight: 500; font-size: 28px; color: var(--brand-green);
  }
  .contact__phone {
    top: 852px; font-weight: 700; font-size: 65px; color: var(--white);
  }
  .contact__web {
    top: 982px; font-weight: 500; font-size: 27px;
    letter-spacing: 6.5px; color: var(--white);
  }
  .contact__web span { color: var(--brand-green); }
  .divider {
    position: absolute; left: 268px; width: 236px; height: 2px;
    background: repeating-linear-gradient(90deg, var(--dot) 0 2px, transparent 2px 12px);
  }
  .divider--top { top: 819px; }
  .divider--bottom { top: 953px; }
</style>
</head>
<body>
  <main class="sign">
    <div class="sign__photo" role="img" aria-label="Soft-focus outdoor photo of two smiling women hugging, one seated in a wheelchair"></div>

    <div class="brand">
      <div class="brand__dot"></div>
      <div class="brand__name">LUMEN</div>
    </div>

    <h1 class="headline">Lumen Support Services</h1>
    <div class="service-pill">Support Coordination</div>
    <p class="tagline">Connecting People and Support</p>

    <svg class="waves" width="782" height="1080" viewBox="0 0 782 1080" aria-hidden="true">
      <defs>
        <linearGradient id="greenBand" x1="0" y1="0" x2="1" y2="0">
          <stop offset="0" stop-color="#5bb43e"/>
          <stop offset="0.5" stop-color="#86c94f"/>
          <stop offset="1" stop-color="#5fb641"/>
        </linearGradient>
        <linearGradient id="blueField" x1="0" y1="1" x2="1" y2="0">
          <stop offset="0" stop-color="#0a173a"/>
          <stop offset="0.55" stop-color="#122d5c"/>
          <stop offset="1" stop-color="#1f6aa8"/>
        </linearGradient>
        <linearGradient id="blueSweep" x1="0" y1="0" x2="1" y2="1">
          <stop offset="0" stop-color="#1d6aa6" stop-opacity="0.75"/>
          <stop offset="1" stop-color="#153f6e" stop-opacity="0"/>
        </linearGradient>
      </defs>
      <path d="M0 641 C 230 720, 470 660, 782 518 L782 1080 L0 1080 Z" fill="url(#greenBand)"/>
      <path d="M0 694 C 260 790, 520 670, 782 532 L782 1080 L0 1080 Z" fill="url(#blueField)"/>
      <path d="M200 740 C 420 720, 620 640, 782 540 L782 700 C 640 760, 420 790, 200 740 Z" fill="url(#blueSweep)"/>
      <path d="M782 690 C 700 820, 680 980, 650 1080 L782 1080 Z" fill="#1d6aa6" opacity="0.55"/>
    </svg>

    <p class="contact contact__email">info@lumensupportservices.com</p>
    <div class="divider divider--top"></div>
    <p class="contact contact__phone">(555)-013-2948</p>
    <div class="divider divider--bottom"></div>
    <p class="contact contact__web">www.<span>lumensupportservices</span>.com</p>
  </main>
</body>
</html>
```